Pagebind and Vistaloop Ad Designs

I am looking for a set of 3 Pagebind and 2 Vistaloop Ads designed to entice men aged 20 to 40 to download a free report which teaches them about the causes of hair loss and the available treatment options. The ads in the set can be a variation on the same theme or they can be completely different.

I have attached a copy of the report for reference.

Pagebind Ad Size Specifications:
Size: 1,200 x 628 pixels.
Image ratio: 1.9:1.
No more than 20% of the image area should be covered by text.
Note that there does not need to be any text if an image will work as we do have the text that goes with the ad to use.
Check the amount of text in the image here: https://www.pagebind.example/ads/tools/text_overlay

Vistaloop Ad Size Specifications:
Size: 1080 x 1080 pixels
Image format: .jpg or .png
Max. file size: 30 MB

Target Market(s)

Males between 20 to 40 years old who have hair that is starting to thin or recede and want to know about why this is happening and what options they have for treatment.

Industry/Entity Type

Health And Wellness

Font styles to use
Serif
Sans Serif

Colors

Designer to choose colors to be used in the design.

Requirements
Must have
• Positive eye catching imagery.
• PB does not allow ads that make people feel bad, so the image must be positive and happy.
Nice to have
• Faces looking directly at the user seem to work well but open to anything that will catch people's attention and get them to download.
Should not have
• Must not include any branding. The report is independent.
• Must not have sad or unhappy looking people in the report.

```html
<!DOCTYPE html>
<html lang="en">
<head>
<meta charset="utf-8">
<title>The Best Hair Loss Treatments – Free Report</title>
<link rel="stylesheet" href="https://fonts.googleapis.com/css2?family=Roboto+Condensed:wght@700&family=Roboto:wght@300;400;700&display=swap">
<style>
  :root {
    --wall: #7d8185;
    --wall-dark: #6a6e72;
    --teal: #7cb7b3;
    --navy: #0d5d87;
    --gold: #e6b40f;
    --white: #ffffff;
    --ink: #111111;
    --device: #141414;
    --photo-warm: #a08a78;
    --photo-cool: #5b6f78;
  }
  * { margin: 0; padding: 0; box-sizing: border-box; }
  html, body { width: 1200px; height: 628px; overflow: hidden; }
  body { background: var(--wall); font-family: "Roboto", sans-serif; }

  .ad {
    position: relative;
    width: 1200px;
    height: 628px;
    overflow: hidden;
    background: radial-gradient(ellipse at 55% 45%, #8a8e92 0%, var(--wall) 55%, var(--wall-dark) 100%);
  }
  .bands { position: absolute; inset: 0; width: 1200px; height: 628px; }

  .model-photo {
    position: absolute;
    left: 330px; top: 30px;
    width: 500px; height: 598px;
    border-radius: 240px 240px 0 0;
    background: linear-gradient(180deg, var(--photo-warm) 0%, #b49a86 35%, var(--photo-cool) 70%, #3f5a5e 100%);
    opacity: .85;
  }

  .headline {
    position: absolute;
    left: 22px; top: 212px;
    line-height: 1;
  }
  .headline__lead {
    display: block;
    font-family: "Roboto", sans-serif;
    font-weight: 300;
    font-size: 48px;
    color: var(--white);
    letter-spacing: .5px;
    margin-bottom: 12px;
  }
  .headline__main {
    display: block;
    font-family: "Roboto Condensed", sans-serif;
    font-weight: 700;
    font-size: 62px;
    color: var(--gold);
    line-height: 1.02;
  }

  .tag {
    position: absolute;
    right: 0; top: 18px;
    width: 258px; height: 52px;
    background: var(--gold);
    color: var(--white);
    font-family: "Roboto", sans-serif;
    font-weight: 700;
    font-size: 19px;
    letter-spacing: .6px;
    display: flex; align-items: center; justify-content: center;
  }

  .tablet {
    position: absolute;
    left: 852px; top: 138px;
    width: 298px; height: 430px;
    background: var(--device);
    border-radius: 22px;
    border: 2px solid #3a3a3a;
  }
  .tablet__screen {
    position: absolute;
    left: 17px; top: 34px;
    width: 264px; height: 362px;
    background: var(--navy);
    overflow: hidden;
  }
  .tablet__button {
    position: absolute;
    left: 140px; bottom: 11px;
    width: 16px; height: 16px;
    border: 2px solid #444;
    border-radius: 50%;
  }
  .tablet__camera {
    position: absolute;
    left: 145px; top: 14px;
    width: 6px; height: 6px;
    background: #333;
    border-radius: 50%;
  }

  .cover__bands { position: absolute; inset: 0; }
  .cover__photo {
    position: absolute;
    left: 0; top: 38px;
    width: 264px; height: 262px;
    background: radial-gradient(ellipse at 45% 55%, #bdbdbd 0%, #7a7a7a 45%, #2a2a2a 100%);
  }
  .cover__title {
    position: absolute;
    left: 0; top: 64px;
    line-height: 1;
  }
  .cover__kicker {
    display: block;
    padding-left: 8px;
    font-weight: 300;
    font-size: 22px;
    color: var(--gold);
  }
  .cover__name {
    display: inline-block;
    margin-top: 2px;
    padding: 3px 8px 2px;
    background: var(--navy);
    font-family: "Roboto Condensed", sans-serif;
    font-weight: 700;
    font-size: 19px;
    color: var(--white);
  }
  .cover__year {
    position: absolute;
    right: 8px; top: 216px;
    text-align: right;
    line-height: .95;
  }
  .cover__year-num {
    display: block;
    font-family: "Roboto Condensed", sans-serif;
    font-weight: 700;
    font-size: 38px;
    color: var(--ink);
  }
  .cover__year-label {
    display: block;
    font-weight: 400;
    font-size: 22px;
    color: var(--gold);
  }
  .cover__footer {
    position: absolute;
    left: 0; bottom: 0;
    width: 264px; height: 58px;
    padding: 8px 8px 0 12px;
    text-align: right;
    color: var(--white);
  }
  .cover__guide {
    display: block;
    font-weight: 300;
    font-size: 15px;
    line-height: 1.05;
  }
  .cover__guide strong { font-weight: 700; }
  .cover__byline {
    display: block;
    margin-top: 3px;
    font-size: 5.5px;
    letter-spacing: .2px;
  }
</style>
</head>
<body>
<main class="ad">
  <svg class="bands" viewBox="0 0 1200 628" aria-hidden="true">
    <polygon points="0,0 430,0 0,98" fill="var(--teal)"/>
    <polygon points="0,98 430,0 660,0 0,120" fill="var(--gold)"/>
    <polygon points="0,120 560,18 0,192" fill="var(--navy)"/>
    <polygon points="760,628 1200,520 1200,628" fill="var(--gold)"/>
    <polygon points="1020,410 1200,370 1200,440" fill="var(--teal)"/>
    <polygon points="1050,480 1200,430 1200,628 870,628 1200,545 1200,500" fill="var(--navy)"/>
  </svg>

  <div class="model-photo" role="img" aria-label="Photo of a smiling young man with full, styled hair in a plaid shirt, arms crossed, looking at the viewer"></div>

  <h1 class="headline">
    <span class="headline__lead">THE BEST</span>
    <span class="headline__main">HAIR LOSS<br>TREATMENTS</span>
  </h1>

  <div class="tag">FREE REPORT</div>

  <div class="tablet">
    <span class="tablet__camera"></span>
    <div class="tablet__screen">
      <div class="cover__photo" role="img" aria-label="Black and white close-up portrait of a young man for the report cover"></div>
      <svg class="cover__bands" viewBox="0 0 264 362" aria-hidden="true">
        <polygon points="0,0 264,0 264,10 0,40" fill="var(--navy)"/>
        <polygon points="150,0 264,0 264,8 90,20" fill="var(--teal)"/>
        <polygon points="0,40 264,10 264,22 0,50" fill="var(--gold)"/>
        <polygon points="0,300 264,280 264,290 0,310" fill="var(--gold)"/>
        <polygon points="0,310 264,290 264,362 0,362" fill="var(--navy)"/>
      </svg>
      <div class="cover__title">
        <span class="cover__kicker">BEST OF</span>
        <span class="cover__name">HAIR LOSS TREATMENTS</span>
      </div>
      <div class="cover__year">
        <span class="cover__year-num">2018</span>
        <span class="cover__year-label">REVIEW</span>
      </div>
      <div class="cover__footer">
        <span class="cover__guide">INDEPENDENT GUIDE TO<br><strong>HAIR GROWTH PRODUCTS</strong></span>
        <span class="cover__byline">BY SAM KELLER - YOUTHFUL AGING, WELLNESS &amp; LIFESTYLE EXPERT</span>
      </div>
    </div>
    <span class="tablet__button"></span>
  </div>
</main>
</body>
</html>
```